Energy Solution company Needs a PowerPoint Design

We need a PowerPoint design for new energy solution company based in Houston. major markets / clients in Africa called ''RV Mavrek Solutions'' . We provider variety of professional services, systems ,and project management solutions to Oil & Gas, Power , Telecommunication , ICT, Airlines & Transportation , Social & Public Sector and Utilities & Alternative Energy industries. We would like to see a simple PowerPoint designs but statement. The final design should communicate engineering Integrity, quality and safety. See attached file with template and company logo. please use logo color combination.

Target Market(s)

Oil & Gas, Power , Telecommunication , ICT, Airlines & Transportation , Social & Public Sector and Utilities & Alternative Energy industries.

Industry/Entity Type

It Company

Font styles to use
Other font styles liked:
• Century Gothic

Colors
ffc214
aaaaaa
0355a3

Requirements
Must have
• engineering details oriented simple looks. SEE ATTACHED PPT WITH COMPANY LOGO AND TEMPLATE. PLEASE ATTACHED LOGO COLOR COMBINATION.]
• We will like to see 5 text boxes with different images across the middle of the cover page, this images will be from below Industries:
• • Oil and Gas
• • Power
• • Information Technology
• • Manufacturing Industry
• • Higher Education Industry
• Please don't include the Industries name as list above, We just want the images.
Nice to have
• • Oil and Gas
• • Power

```html
<!DOCTYPE html>
<html lang="en">
<head>
<meta charset="utf-8">
<title>RV Mavrek Solutions – Project Slide</title>
<link rel="stylesheet" href="https://fonts.googleapis.com/css2?family=Roboto:wght@400;500;700&display=swap">
<style>
  :root {
    --header-blue: #03436d;
    --subtitle-blue: #0d4a74;
    --body-ink: #1e1e1e;
    --paper: #ffffff;
    --footer-grey: #8f8f8f;
  }
  * { box-sizing: border-box; margin: 0; padding: 0; }
  html, body {
    width: 1200px;
    height: 900px;
    overflow: hidden;
    background: var(--paper);
  }
  .slide {
    position: relative;
    width: 1200px;
    height: 900px;
    background: var(--paper);
    font-family: "Roboto", Arial, sans-serif;
  }
  .slide-header {
    position: absolute;
    top: 0; left: 0;
    width: 1200px;
    height: 112px;
    background: var(--header-blue);
    display: flex;
    align-items: center;
    justify-content: space-between;
    padding: 0 27px;
  }
  .slide-title {
    color: var(--paper);
    font-size: 54px;
    font-weight: 500;
    letter-spacing: 0.2px;
    line-height: 1;
    margin-top: -4px;
  }
  .brand-name {
    color: var(--paper);
    font-size: 22px;
    font-weight: 700;
    line-height: 1;
  }
  .content-column {
    position: absolute;
    top: 186px;
    width: 545px;
  }
  .content-column.left { left: 52px; }
  .content-column.right { left: 626px; }
  .column-subtitle {
    color: var(--subtitle-blue);
    font-size: 25px;
    font-weight: 500;
    line-height: 36px;
  }
  .column-text {
    color: var(--body-ink);
    font-size: 20.5px;
    line-height: 36px;
    white-space: pre;
  }
  .column-text + .column-text { margin-top: 36px; }
  .slide-footer {
    position: absolute;
    left: 0; bottom: 0;
    width: 1200px;
    height: 45px;
    background: var(--footer-grey);
  }
</style>
</head>
<body>
<main class="slide">
  <header class="slide-header">
    <h1 class="slide-title">Project Title Here</h1>
    <span class="brand-name">RV Mavrek Solutions</span>
  </header>

  <section class="content-column left">
    <h2 class="column-subtitle">Project Subtitle Here</h2>
    <p class="column-text">Lorem ipsum dolor sit Lorem ipsum dolor sit  Lorem
ipsum dolor sit Lorem ipsum dolor sit  Lorem ipsum
dolor sit Lorem ipsum dolor  Lorem ipsum dolor sit
Lorem ipsum dolor sit  Lorem ipsum dolor sit Lorem
ipsum dolor sit  Lorem ipsum dolor sit Lorem ipsum
dolor  Lorem ipsum dolor sit Lorem ipsum dolor sit
Lorem ipsum dolor sit Lorem ipsum dolor sit   Lorem
ipsum dolor sit Lorem ipsum dolor sit  Lorem ipsum
dolor sit Lorem ipsum dolor  Lorem ipsum dolor sit
Lorem ipsum dolor sit  Lorem ipsum dolor sit Lorem
ipsum dolor sit</p>
    <p class="column-text"> Lorem ipsum dolor sit Lorem ipsum dolor sit  Lorem
ipsum dolor sit Lorem ipsum dolor  Lorem ipsum dolor
sit Lorem ipsum dolor sit  Lorem ipsum dolor sit Lorem</p>
  </section>

  <section class="content-column right">
    <h2 class="column-subtitle">Project Subtitle Here</h2>
    <p class="column-text">Lorem ipsum dolor sit Lorem ipsum dolor sit  Lorem
ipsum dolor sit Lorem ipsum dolor sit  Lorem ipsum
dolor sit Lorem ipsum dolor  Lorem ipsum dolor sit
Lorem ipsum dolor sit  Lorem ipsum dolor sit Lorem
ipsum dolor sit  Lorem ipsum dolor sit Lorem ipsum
dolor  Lorem ipsum dolor sit Lorem ipsum dolor sit
Lorem ipsum dolor sit Lorem ipsum dolor sit   Lorem
ipsum dolor sit Lorem ipsum dolor sit  Lorem ipsum
dolor sit Lorem ipsum dolor  Lorem ipsum dolor sit
Lorem ipsum dolor sit  Lorem ipsum dolor sit Lorem
ipsum dolor sit</p>
    <p class="column-text"> Lorem ipsum dolor sit Lorem ipsum dolor sit  Lorem
ipsum dolor sit Lorem ipsum dolor  Lorem ipsum dolor
sit Lorem ipsum dolor sit  Lorem ipsum dolor sit Lorem</p>
  </section>

  <footer class="slide-footer"></footer>
</main>
</body>
</html>
```